Bookmark Design

We would like to design a book mark with logos of our two business and a quote.

One side with the quote "The first wealth is health" - Tobias Quill Harrow and the two logos.

The back side has the two logos with its respective phone numbers and a common address (this is to be advised to the winner of the project).

```html
<!DOCTYPE html>
<html lang="en">
<head>
<meta charset="utf-8">
<title>Brightmere Clinic &amp; Harbour Dental Bookmark</title>
<link rel="stylesheet" href="https://fonts.googleapis.com/css2?family=Bebas+Neue&family=Oswald:wght@300;500;600&display=swap">
<style>
  :root {
    --backdrop: #9a9a9a;
    --paper: #ffffff;
    --brand-blue: #0b4fa8;
    --brand-green: #8ac847;
    --dental-green: #5cb85f;
    --slate: #535d60;
  }
  * { box-sizing: border-box; margin: 0; padding: 0; }
  html, body {
    width: 1073px;
    height: 1200px;
    overflow: hidden;
    background: var(--backdrop);
  }
  .bookmark {
    position: absolute;
    top: 117px;
    width: 322px;
    height: 966px;
    background: var(--paper);
    overflow: hidden;
  }
  .bookmark--front { left: 164px; }
  .bookmark--back { left: 586px; }
  .bookmark__shapes {
    position: absolute;
    inset: 0;
    width: 322px;
    height: 966px;
  }

  /* Brand name stand-ins */
  .clinic-mark {
    position: absolute;
    left: 0;
    width: 322px;
    text-align: center;
    font-family: "Oswald", sans-serif;
    font-weight: 600;
    color: var(--brand-blue);
    font-size: 19px;
    line-height: 20px;
    letter-spacing: 1px;
  }
  .clinic-mark__dot {
    display: block;
    width: 88px;
    height: 88px;
    margin: 0 auto 12px;
    border: 3px solid var(--brand-blue);
    border-radius: 50%;
  }
  .dental-mark {
    position: absolute;
    left: 0;
    width: 322px;
    text-align: center;
    font-family: "Oswald", sans-serif;
    font-weight: 600;
    color: var(--dental-green);
    font-size: 24px;
    line-height: 28px;
    letter-spacing: 0.5px;
  }

  /* Front */
  .quote {
    position: absolute;
    left: 50px;
    top: 224px;
    color: var(--paper);
  }
  .quote__text {
    position: relative;
    font-family: "Bebas Neue", sans-serif;
    font-size: 78px;
    line-height: 91px;
    text-transform: uppercase;
    white-space: nowrap;
  }
  .quote__mark--open {
    position: absolute;
    left: -28px;
    top: -8px;
    font-size: 60px;
  }
  .quote__mark--close {
    font-size: 60px;
    vertical-align: 18px;
    margin-left: 4px;
  }
  .quote__author {
    margin-top: 8px;
    font-family: "Oswald", sans-serif;
    font-weight: 500;
    font-size: 21px;
    letter-spacing: -0.3px;
    transform: scaleX(0.85);
    transform-origin: left center;
  }

  /* Back */
  .contact-icon {
    position: absolute;
    left: 144px;
    width: 35px;
    height: 35px;
  }
  .phone-number {
    position: absolute;
    left: 0;
    width: 322px;
    text-align: center;
    font-family: "Bebas Neue", sans-serif;
    font-size: 48px;
    line-height: 48px;
    color: var(--paper);
    letter-spacing: 0.5px;
  }
  .address {
    position: absolute;
    left: 21px;
    top: 421px;
    width: 281px;
    height: 63px;
    border: 2px solid var(--paper);
    border-top: none;
    text-align: center;
    color: var(--paper);
    font-family: "Oswald", sans-serif;
    font-weight: 300;
    font-size: 22px;
    line-height: 32px;
  }
  .address::before,
  .address::after {
    content: "";
    position: absolute;
    top: 0;
    width: 47px;
    border-top: 2px solid var(--paper);
  }
  .address::before { left: -2px; }
  .address::after { right: -2px; }
  .address__line { display: block; }
  .address__line--first { margin-top: -16px; }
</style>
</head>
<body>

<section class="bookmark bookmark--front" aria-label="Bookmark front">
  <svg class="bookmark__shapes" viewBox="0 0 322 966" aria-hidden="true">
    <circle cx="71" cy="507" r="320" fill="var(--brand-green)"/>
    <circle cx="56" cy="464" r="275" fill="var(--slate)"/>
    <circle cx="47" cy="454" r="266" fill="var(--brand-blue)"/>
  </svg>

  <div class="clinic-mark" style="top:38px;">
    <span class="clinic-mark__dot"></span>
    BRIGHTMERE CLINIC
  </div>

  <blockquote class="quote">
    <p class="quote__text"><span class="quote__mark--open">"</span>The<br>First<br>Wealth is<br>Health<span class="quote__mark--close">"</span></p>
    <p class="quote__author">- Tobias Quill Harrow</p>
  </blockquote>

  <div class="dental-mark" style="top:852px;">HARBOUR DENTAL<br>BRIGHTMERE</div>
</section>

<section class="bookmark bookmark--back" aria-label="Bookmark back">
  <svg class="bookmark__shapes" viewBox="0 0 322 966" aria-hidden="true">
    <rect width="322" height="966" fill="var(--brand-green)"/>
    <path d="M157 0 H322 V78 Q250 20 157 0 Z" fill="var(--slate)"/>
    <path d="M0 78 Q161 10 322 78 V966 H0 Z" fill="var(--brand-blue)"/>
    <circle cx="74" cy="815" r="285" fill="var(--brand-green)"/>
    <circle cx="51" cy="803" r="271" fill="var(--paper)"/>
  </svg>

  <svg class="contact-icon" style="top:110px;" viewBox="0 0 36 36" aria-hidden="true">
    <circle cx="18" cy="18" r="18" fill="var(--paper)"/>
    <path d="M12 11 l3 -1 2 4 -2 1.5 q1.5 3.5 5 5 l1.5 -2 4 2 -1 3 q-7 1 -12.5 -12.5 z" fill="var(--brand-green)"/>
  </svg>
  <p class="phone-number" style="top:160px;">03 9000 4817</p>

  <svg class="contact-icon" style="top:241px;" viewBox="0 0 36 36" aria-hidden="true">
    <circle cx="18" cy="18" r="18" fill="var(--paper)"/>
    <path d="M12 11 l3 -1 2 4 -2 1.5 q1.5 3.5 5 5 l1.5 -2 4 2 -1 3 q-7 1 -12.5 -12.5 z" fill="var(--brand-green)"/>
  </svg>
  <p class="phone-number" style="top:290px;">61 3 9000 2634</p>

  <svg class="contact-icon" style="top:365px;" viewBox="0 0 36 36" aria-hidden="true">
    <circle cx="18" cy="18" r="18" fill="var(--paper)"/>
    <path d="M18 8 a7 7 0 0 1 7 7 c0 5 -7 12 -7 12 s-7 -7 -7 -12 a7 7 0 0 1 7 -7 z" fill="var(--brand-green)"/>
    <circle cx="18" cy="15" r="2.6" fill="var(--paper)"/>
  </svg>

  <address class="address">
    <span class="address__line address__line--first">12B LINDELL ROAD</span>
    <span class="address__line">BRIGHTMERE, VIC 3990</span>
  </address>

  <div class="clinic-mark" style="top:636px;">
    <span class="clinic-mark__dot" style="width:94px;height:94px;"></span>
    BRIGHTMERE CLINIC
  </div>

  <div class="dental-mark" style="top:838px;">HARBOUR DENTAL<br>BRIGHTMERE</div>
</section>

</body>
</html>
```